Vorna Fleet business card

I am needing a business card that at a glance shows all the services that we provide emphasizing some more than others. We are a Fleet and Compliance management company as well as a software company. We provide outsourced solutions for KPX compliance and HR services via our own software.
In addition, we do
drug testing
GPS
Cameras
Electronic DVIRS
ELD's

Target Market(s)

Transportation company owners

Industry/Entity Type

Transportation supplier

Contact Information for Business Card

the card should inform potential customers what we do

Other font styles liked:
• I have added brand guidelines. See attached

Requirements
Must have
• See description
Should not have
• Colors outside my brand guide. See attached

```html
<!DOCTYPE html>
<html lang="en">
<head>
<meta charset="utf-8">
<title>Vorna Fleet business card</title>
<link rel="stylesheet" href="https://fonts.googleapis.com/css2?family=Poppins:wght@400;500;600&display=swap">
<style>
  :root {
    --brand-red: #e5252f;
    --ink: #111111;
    --card: #fafafa;
    --backdrop: #e7e3dd;
    --band-text: #ffffff;
  }
  * { margin: 0; padding: 0; box-sizing: border-box; }
  html, body {
    width: 900px; height: 1200px; overflow: hidden;
    background: var(--backdrop);
    font-family: "Poppins", sans-serif;
  }
  .canvas { position: relative; width: 900px; height: 1200px; }
  .card {
    position: absolute;
    width: 773px; height: 448px;
    background: var(--card);
    box-shadow: 0 4px 14px rgba(0,0,0,0.18);
  }
  .card-front { left: 72px; top: 135px; }
  .card-back { left: 74px; top: 625px; }

  .front-wordmark {
    position: absolute;
    left: 42px; top: 50px;
    width: 152px; height: 296px;
    display: flex; align-items: center; justify-content: center;
  }
  .front-wordmark span {
    display: block;
    transform: rotate(-90deg);
    white-space: nowrap;
    font-size: 46px; font-weight: 600;
    color: var(--ink);
    letter-spacing: 1px;
  }

  .holder {
    position: absolute; right: 42px; top: 78px;
    text-align: right;
  }
  .holder-name {
    font-size: 28px; font-weight: 500;
    color: var(--brand-red);
    letter-spacing: 1.5px;
    line-height: 36px;
  }
  .holder-title {
    font-size: 21px; font-weight: 400;
    color: var(--ink);
    letter-spacing: 1.5px;
    line-height: 30px;
  }
  .divider {
    position: absolute; left: 218px; right: 42px; top: 178px;
    height: 2px; background: var(--ink);
  }
  .contact {
    position: absolute; right: 42px; top: 214px;
    list-style: none; text-align: right;
    font-size: 20px; color: var(--ink);
    letter-spacing: 1.6px; line-height: 32px;
  }
  .services {
    position: absolute; left: 42px; right: 42px; top: 364px;
    height: 37px;
    background: var(--brand-red);
    color: var(--band-text);
    display: flex; align-items: center; justify-content: space-between;
    padding: 0 14px;
    font-size: 20px; font-weight: 400;
  }

  .back-wordmark {
    position: absolute; inset: 0;
    display: flex; align-items: center; justify-content: center;
    font-size: 96px; font-weight: 600;
    color: var(--ink);
    letter-spacing: 1px;
  }
</style>
</head>
<body>
<main class="canvas">
  <section class="card card-front" aria-label="Card front">
    <div class="front-wordmark"><span>Vorna Fleet</span></div>
    <div class="holder">
      <p class="holder-name">JOHNATHAN DOE</p>
      <p class="holder-title">PRESIDENT</p>
    </div>
    <div class="divider"></div>
    <ul class="contact">
      <li>123 456 789</li>
      <li>contact.email@domain.com</li>
      <li>www.vornafleet.com</li>
    </ul>
    <div class="services">
      <span>Drug Testing</span><span>|</span><span>GPS</span><span>|</span><span>Cameras</span><span>|</span><span>Electronic DVIRS</span><span>|</span><span>ELD's</span>
    </div>
  </section>

  <section class="card card-back" aria-label="Card back">
    <div class="back-wordmark">Vorna Fleet</div>
  </section>
</main>
</body>
</html>
```